Postcard Design

We offer facilitated group glasses in senior living facilities centered around memoir and life story writing. The postcards will go to administrators, activity directors and program directors at facilities, and potentially to librarians, staff and senior centers etc... So we want to say a little bit about WHY life writing is important to this population. I will upload a flyer I made myself. This will give you a sense of what we do and what we are trying to impart.
I've been using bright colors because they appeal to our population - blue is critical (Tinfern Story Circle) and I'm down with anything else.
I have several images from google images that I've been using, but I'm not particularly attached to them. I did buy the rights to the blue owl guy and I have it in several formats and sizes.

I'm also including a power point that describes our course work, though I don't expect you to read it! Just trying to include anything that might be helpful. Any suggestions are most welcome!!! Thanks!

Industry/Entity Type

Group

```html
<!DOCTYPE html>
<html lang="en">
<head>
<meta charset="utf-8">
<title>Tinfern Story Circle – Postcard</title>
<link href="https://fonts.googleapis.com/css2?family=Lato:wght@400;700&family=Playfair+Display:wght@700&display=swap" rel="stylesheet">
<style>
  :root {
    --sky: #2aa9e0;
    --sky-deep: #1b97d2;
    --sky-pale: #eaf6fc;
    --sky-mist: #d4eefa;
    --orange: #ee9b22;
    --rust: #d0621f;
    --ink: #3a3a3a;
    --white: #ffffff;
    --stage: #e4e2de;
  }
  * { box-sizing: border-box; margin: 0; padding: 0; }
  html, body { width: 1200px; height: 900px; overflow: hidden; }
  body { background: var(--stage); font-family: "Lato", sans-serif; color: var(--ink); position: relative; }

  .card { position: absolute; width: 671px; height: 520px; overflow: hidden; background: var(--sky-pale); }
  .card--front { left: 41px; top: 30px; z-index: 2; box-shadow: 0 2px 8px rgba(0,0,0,.18); }
  .card--back { left: 452px; top: 342px; z-index: 1; box-shadow: 0 2px 8px rgba(0,0,0,.18); }

  /* front */
  .hero-photo { position: absolute; left: 250px; top: 0; width: 421px; height: 460px;
    background: linear-gradient(90deg, rgba(234,246,252,1) 0%, rgba(234,246,252,0) 22%),
                linear-gradient(160deg, #f4f1ec 0%, #d9dde6 40%, #c9d3e4 60%, #b9bcc4 85%, #8f949c 100%); }
  .brand { position: absolute; display: flex; align-items: center; gap: 8px;
    font-family: "Lato", sans-serif; font-weight: 700; color: var(--sky); }
  .brand__dot { width: 14px; height: 14px; border-radius: 50%; background: var(--sky); flex: none; }
  .card--front .brand { left: 52px; top: 200px; font-size: 24px; }

  .headline-panel { position: absolute; left: 0; top: 242px; width: 407px; height: 198px;
    background: rgba(42,169,224,.95); border-top-right-radius: 26px; border-bottom-right-radius: 8px; padding: 8px 0 0 38px; }
  .headline { font-family: "Playfair Display", serif; font-weight: 700; color: var(--white);
    font-size: 54px; line-height: 54px; letter-spacing: .5px; }
  .headline-rule { width: 336px; border-top: 2px dotted rgba(255,255,255,.8); margin: 10px 0 8px; }
  .tagline { color: var(--white); font-weight: 700; font-size: 22px; line-height: 28px; }

  .footer-band { position: absolute; left: 0; bottom: 0; width: 100%; height: 48px; background: var(--orange); }
  .front-contacts { color: var(--white); font-weight: 700; font-size: 15px; line-height: 48px; padding-left: 108px; word-spacing: 1px; }
  .front-contacts span { margin-right: 10px; }

  /* back */
  .benefits-column { position: absolute; left: 0; top: 0; width: 330px; height: 472px;
    background: linear-gradient(180deg, var(--sky) 0%, #5cbde8 25%, var(--sky-mist) 55%, var(--sky-pale) 75%); }
  .benefits-column::after { content: ""; position: absolute; right: 0; top: 0; width: 26px; height: 60%;
    background: linear-gradient(180deg, var(--sky-deep), rgba(27,151,210,0)); }
  .benefits { position: absolute; left: 50px; top: 54px; width: 253px; list-style: none;
    font-size: 13px; line-height: 16px; text-align: justify; color: var(--ink); }
  .benefits li { position: relative; padding-left: 16px; margin-bottom: 0; }
  .benefits li::before { content: ""; position: absolute; left: 1px; top: 5px; width: 7px; height: 7px; border-radius: 50%; background: var(--sky); }

  .group-photo { position: absolute; left: 328px; top: 36px; width: 308px; height: 216px; background: var(--white);
    padding: 8px; transform: rotate(-3deg); box-shadow: 0 2px 6px rgba(0,0,0,.25); }
  .group-photo__fill { width: 100%; height: 100%;
    background: linear-gradient(170deg, #8d7a62 0%, #c7b79e 30%, #e9e2d6 55%, #9fb2c9 75%, #5f6f8a 100%); }

  .join-line { position: absolute; left: 46px; top: 352px; font-size: 14px; }
  .big-phone { position: absolute; left: 44px; top: 364px; font-family: "Playfair Display", serif; font-weight: 700;
    font-size: 56px; line-height: 64px; color: var(--rust); letter-spacing: -0.5px; }
  .web-line { position: absolute; left: 62px; top: 432px; display: flex; align-items: center; gap: 6px;
    font-weight: 700; font-size: 17px; }
  .web-line svg { flex: none; }
  .web-line .gap { width: 6px; }

  .card--back .brand { left: 452px; top: 357px; font-size: 19px; }
  .address { position: absolute; left: 470px; top: 394px; font-size: 12px; line-height: 14px; padding-left: 16px; }
  .address svg { position: absolute; left: 0; top: 1px; }
</style>
</head>
<body>

<section class="card card--back" aria-label="Postcard back">
  <div class="benefits-column">
    <ul class="benefits">
      <li>Helps participants make meaning of each key life event</li>
      <li>Shown to sharpen memory, lift mood and improve a sense of personal control</li>
      <li>Builds confidence and overall life satisfaction</li>
      <li>Improves self-esteem and lowers depression</li>
      <li>Furthers personal growth and promotes self-discovery</li>
      <li>Promotes social engagements</li>
      <li>Help the older adults in your life create a permanent historical record about their lives and to pass on their wisdom and values to future generations.</li>
    </ul>
  </div>

  <figure class="group-photo">
    <div class="group-photo__fill" role="img" aria-label="Photo of a group of seniors seated around a table in a writing circle"></div>
  </figure>

  <p class="join-line">If you want to join our community you can contact us at</p>
  <p class="big-phone">555-214-0387</p>
  <p class="web-line">
    <svg width="16" height="12" viewBox="0 0 16 12" aria-hidden="true"><rect x="0.5" y="0.5" width="15" height="11" fill="none" stroke="#3a3a3a"/><path d="M0.5 0.5 8 7 15.5 0.5" fill="none" stroke="#3a3a3a"/></svg>
    ruth@tinfern.biz
    <span class="gap"></span>
    <svg width="16" height="16" viewBox="0 0 16 16" aria-hidden="true"><circle cx="7" cy="7" r="5" fill="none" stroke="#3a3a3a" stroke-width="1.6"/><line x1="10.5" y1="10.5" x2="15" y2="15" stroke="#3a3a3a" stroke-width="2"/></svg>
    www.tinfern.biz
  </p>

  <div class="brand"><span class="brand__dot"></span>Tinfern Story Circle</div>
  <address class="address" style="font-style:normal">
    <svg width="11" height="14" viewBox="0 0 11 14" aria-hidden="true"><path d="M5.5 0C2.5 0 0 2.4 0 5.4 0 9.3 5.5 14 5.5 14S11 9.3 11 5.4C11 2.4 8.5 0 5.5 0Z" fill="#3a3a3a"/><circle cx="5.5" cy="5.3" r="2" fill="#fff"/></svg>
    Harlow Post Shop<br>P.O. Box 4418<br>Harlow Centre, 2190
  </address>

  <div class="footer-band"></div>
</section>

<section class="card card--front" aria-label="Postcard front">
  <div class="hero-photo" role="img" aria-label="Photo of three smiling seniors gathered around a laptop"></div>

  <div class="brand"><span class="brand__dot"></span>Tinfern Story Circle</div>

  <div class="headline-panel">
    <h1 class="headline">Let’s Sharing<br>our Stories</h1>
    <div class="headline-rule"></div>
    <p class="tagline">Everyone has a story to tell but<br>most of us need help telling it.</p>
  </div>

  <div class="footer-band">
    <p class="front-contacts"><span>Ruth Calloway Ph 555-214-0387</span><span>ruth@tinfern.biz</span> <span>www.tinfern.biz</span></p>
  </div>
</section>

</body>
</html>
```